Website Design for Door Distributor

Garnet Door Design LLC distributes doors in the Southwestern region of the United States. We need a website design for our company launch.

We are looking for a website design that screams modern, and is easy to navigate. We want our customers to browse through our collections of doors with ease, while at the same time enjoy the feel of the website (more on how the website should feel below). Our logo is attached to help with the design process.

We expect this relationship to continue beyond the initial assignment, whether it includes additions or updates to the site. In that sense, we will only work with that designer who will specifically incorporate our ideas into the design, not a designer that submits a "one-size-fits-all" design. With that in mind, we are looking for a creative person who is willing to take some risks.

We are committed to minimizing the amount of revisions needed, so we encourage you to message us with any questions you may have throughout the process, especially in the earlier phases.

Thanks in advance for your time.

Target Market(s)

Home builders, commercial builders, developers, and upper-middle class/upper class customers. As you can see, our target market is of a more sophisticated type, so the design should be on the more serious side, and less playful. It should showcase a sense of class.

Industry/Entity Type

It Company

Requirements
Must have
• The home page should have a slideshow showcasing 4 to 5 different topics. See www.brivaleno.net for an example. The headings for each picture should be easily customizable (font, color, etc.). The user should also be able to click on the picture and be taken to the page that the pictures are linked to.

At the very top right of every page, there should be 2 header links: Download Brochure | Contact

There should be 5 static categories placed in one row at the top of each page. See www.tusk-ravo.com for an example. Each of these categories should drop down when you rest your mouse over it and display a list of links. Again, this should be easily customizable and shown on every page of the site. This will serve as the navigation menu. Let us know if you need to know the exact amount of links for each category - hopefully we can customize it on our end fairly easily.

Categories: Home | Products | Gallery | Support | About Us

Home Page: Along with the above, the home page should include a welcome section that introduces the user to the site. There should also be sections for "Featured Product" and "Testimonial".

Featured product: this will include an image and short text.

Testimonial: this will include a quote, which should be easy for us to update weekly, and a link to "More Testimonials".
Should not have
• No clutter - instead, the design layout should be open and easy to navigate.

No cartoonish graphics - instead, the graphics should be sophisticated and modern.

No flash, no java.

```html
<!DOCTYPE html>
<html lang="en">
<head>
<meta charset="utf-8">
<title>Garnet Door Design</title>
<link href="https://fonts.googleapis.com/css2?family=Carlito:wght@400;700&display=swap" rel="stylesheet">
<style>
:root{
  --page:#f7f7f7;
  --white:#ffffff;
  --brown:#9b6430;
  --brown-dark:#4e2a10;
  --heading:#5a3310;
  --text:#777777;
  --rule:#cfcfcf;
  --nav-top:#8a5a2b;
  --nav-bottom:#5e3815;
}
*{box-sizing:border-box;margin:0;padding:0}
html,body{width:1101px;height:1200px;overflow:hidden}
body{background:var(--page);font-family:'Carlito',sans-serif;color:var(--text);position:relative}
a{color:inherit;text-decoration:none}
.site-header{position:absolute;left:0;top:0;width:1101px;height:105px;background:var(--white);border-bottom:1px solid #e2e2e2}
.brand{position:absolute;left:110px;top:36px;display:flex;align-items:center;gap:8px;color:var(--heading);font-size:19px;font-weight:700;letter-spacing:.3px}
.brand-mark{width:12px;height:12px;background:var(--brown)}
.util-links{position:absolute;right:110px;top:21px;font-size:12.5px;color:#555}
.util-links span{margin:0 4px;color:#888}
.call-now{position:absolute;right:110px;top:68px;font-size:21px;color:#666}
.main-nav{position:absolute;left:110px;top:105px;width:881px;height:45px;
  background:repeating-linear-gradient(135deg,rgba(255,255,255,.05) 0 2px,transparent 2px 4px),linear-gradient(var(--nav-top),var(--nav-bottom));
  border-bottom:3px solid #c9a47a}
.main-nav ul{list-style:none;display:flex;height:100%}
.main-nav li{color:var(--white);font-weight:700;font-size:16px;line-height:42px;text-align:center;border-right:1px solid rgba(0,0,0,.35);box-shadow:1px 0 0 rgba(255,255,255,.12)}
.nav-home{width:85px}
.nav-products{width:123px}
.nav-gallery{width:106px}
.nav-support{width:110px}
.nav-about{width:110px;border-right:none!important;box-shadow:none!important}
.search{position:absolute;left:662px;top:9px;width:208px;height:25px;border-radius:4px;background:#4a2a0e;color:#8a6a4a;font-size:11px;padding-left:7px;line-height:25px}
.hero{position:absolute;left:110px;top:155px;width:881px;height:370px;
  background:linear-gradient(90deg,#e9e2cf 0%,#a0531f 18%,#c9a677 38%,#dcd0b5 55%,#b9854a 72%,#8d3c14 88%,#6b2a0e 100%)}
.hero-floor{position:absolute;left:0;bottom:0;width:100%;height:35%;background:linear-gradient(#c98a45,#a25a22);opacity:.55}
.hero-caption{position:absolute;left:23px;top:116px;width:316px;height:130px;background:rgba(30,30,30,.82);color:var(--white);font-size:17.5px;line-height:25.7px;padding:33px 21px 0}
.hero-dots{position:absolute;left:23px;top:266px;display:flex;gap:3px}
.hero-dots i{width:12px;height:12px;border-radius:50%;background:#333;border:1px solid #777}
.hero-dots i.active{background:#fff;border:2px solid #333}
.welcome{position:absolute;left:119px;top:551px;width:569px}
.section-title{color:var(--heading);font-size:15.5px;font-weight:700;padding-bottom:8px;border-bottom:1px solid var(--rule)}
.welcome p{font-size:11.9px;line-height:22px;margin-top:7px;width:552px}
.welcome p+p{margin-top:0}
.testimonials{position:absolute;left:706px;top:547px;width:276px;height:282px;background:var(--brown);border-radius:4px;padding:11px 26px 0 22px;color:var(--white)}
.testimonials h2{font-size:15.5px;font-weight:700}
.quote-mark{display:block;margin-top:14px}
.testimonials p{font-size:11.9px;line-height:22px;margin-top:2px}
.btn-more{display:inline-block;margin-top:10px;background:var(--brown-dark);color:var(--white);font-size:12.5px;padding:0 14px;height:33px;line-height:33px;border-radius:3px}
.featured{position:absolute;left:119px;top:878px;width:863px}
.featured .section-title{padding-bottom:9px}
.product-grid{display:flex;justify-content:space-between;margin-top:10px}
.product{width:202px}
.product-photo{height:110px;border-radius:4px}
.product p{font-size:11.9px;line-height:22px;margin-top:13px}
.site-footer{position:absolute;left:0;top:1124px;width:1101px;height:76px;background:var(--brown);color:var(--white)}
.footer-links{position:absolute;left:119px;top:15px;font-size:12.3px}
.footer-links span{margin:0 4px}
.copyright{position:absolute;left:119px;top:45px;font-size:12.3px}
.social{position:absolute;left:924px;top:25px;display:flex;gap:5px}
.social i{width:26px;height:26px;border-radius:50%;background:var(--white)}
</style>
</head>
<body>
<header class="site-header">
  <div class="brand"><span class="brand-mark"></span>Garnet Door Design</div>
  <nav class="util-links"><a href="#">Download Brochure</a><span>|</span><a href="#">Contact</a></nav>
  <div class="call-now">Call Now: 1-800-555-0148</div>
</header>

<nav class="main-nav">
  <ul>
    <li class="nav-home">HOME</li><li class="nav-products">PRODUCTS</li><li class="nav-gallery">GALLERY</li><li class="nav-support">SUPPORT</li><li class="nav-about">ABOUT US</li>
  </ul>
  <div class="search">Search</div>
</nav>

<section class="hero" role="img" aria-label="Living room with wooden glass folding doors opening onto a lounge, white orchids in the foreground">
  <div class="hero-floor"></div>
  <div class="hero-caption">Neque porro quisquam est qui dolorem ipsum quia dolor sit amet, consectetur, adipisci velit...</div>
  <div class="hero-dots"><i class="active"></i><i></i><i></i><i></i></div>
</section>

<section class="welcome">
  <h1 class="section-title">WELCOME TO GARNET DOOR DESIGN</h1>
  <p>Lorem Ipsum is simply dummy text of the printing and typesetting industry. Lorem Ipsum has been the industry's standard dummy text ever since the 1500s, when an unknown printer took a galley of type and scrambled it to make a type specimen book. It has survived not only five centuries, but also the leap into electronic typesetting, remaining essentially unchanged. It was popularised in the 1960s with the release of Larkset sheets containing Lorem Ipsum passages, and more recently with desktop publishing software like Veltro PageForm including versions of Lorem Ipsum.</p>
  <p>Lorem Ipsum is simply dummy text of the printing and typesetting industry. Lorem Ipsum has been the industry's standard dummy text ever since the 1500s, when an unknown printer took a galley of type and scrambled it to make a type specimen book. It has survived not only five centuries, but also the leap into electronic typesetting, remaining essentially unchanged. It was popularised in the 1960s with the release of Larkset sheets containing Lorem Ipsum passages, and more recently with desktop publishing .</p>
</section>

<aside class="testimonials">
  <h2>TESTIMONIALS</h2>
  <svg class="quote-mark" width="34" height="26" viewBox="0 0 34 26" aria-hidden="true">
    <path d="M2 24 C0 14 4 6 13 2 L14 5 C9 8 8 11 8 13 A6 6 0 1 1 2 24Z M19 24 C17 14 21 6 30 2 L31 5 C26 8 25 11 25 13 A6 6 0 1 1 19 24Z" fill="#fff"/>
  </svg>
  <p>Lorem Ipsum is simply dummy text of the printing and typesetting industry. Lorem Ipsum has been the industry's standard dummy text ever since the 1500s, when an unknown printer took a galley of type and scrambled it to make a type specimen book. It has survived not only five centurie &nbsp;...</p>
  <a class="btn-more" href="#">More Testimonials</a>
</aside>

<section class="featured">
  <h2 class="section-title">FEATURED PRODUCTS</h2>
  <div class="product-grid">
    <div class="product">
      <div class="product-photo" role="img" aria-label="Carved wooden double front door with wall lanterns" style="background:linear-gradient(90deg,#3a2a1a,#8a4a1e 20%,#a35a24 50%,#8a4a1e 80%,#3a2a1a)"></div>
      <p>Lorem Ipsum is simply dummy text of the printing and typesetting industry.</p>
    </div>
    <div class="product">
      <div class="product-photo" role="img" aria-label="Wooden entry door with leaded glass sidelights" style="background:linear-gradient(90deg,#6a3a22,#a8582a 30%,#c06a30 55%,#9a4e22 80%,#6a3a22)"></div>
      <p>Lorem Ipsum is simply dummy text of the printing and typesetting industry.</p>
    </div>
    <div class="product">
      <div class="product-photo" role="img" aria-label="Wooden front door with oval glass set in grey siding" style="background:linear-gradient(90deg,#8a94a4,#9aa2ae 25%,#8a3e1c 40%,#a24a22 60%,#8a94a4 78%,#7a8494)"></div>
      <p>Lorem Ipsum is simply dummy text of the printing and typesetting industry.</p>
    </div>
    <div class="product">
      <div class="product-photo" role="img" aria-label="Glass patio door with wooden frame opening to a garden" style="background:linear-gradient(90deg,#e6dcc2,#c8a060 30%,#7a2e10 45%,#d8cfa8 65%,#8a3a18 90%,#6a3422)"></div>
      <p>Lorem Ipsum is simply dummy text of the printing and typesetting industry.</p>
    </div>
  </div>
</section>

<footer class="site-footer">
  <nav class="footer-links"><a href="#">Home</a><span>|</span><a href="#">Products</a><span>|</span><a href="#">Gallery</a><span>|</span><a href="#">Support</a><span>|</span><a href="#">About Us</a></nav>
  <div class="copyright">Copyright ©2013 Company Name &nbsp;- All rights reserved</div>
  <div class="social"><i></i><i></i></div>
</footer>
</body>
</html>
```